Online-Portal braucht 2 Banner
Zielgruppe
Wir unterstützen Jugendliche bei der Suche nach Ausbildungsplätzen und Dualen Studienplätzen. Dafür bieten wir einen Stellenmarkt, einen Berufswahltest und jede Menge Informationen zu den Themen Berufe und Bewerbung.
Aufgabenstellung
Für unseren Blog benötigen wir 2 Banner, um verschiedene Bereiche unseres Portals www.lernkompass-jobs.de zu bewerben.
Die Zielseiten:
http://www.lernkompass-jobs.de/bewerbung/
Dies ist eine Überblicksseite für unser "Bewerbungstutorial". Schüler finden hier Informationen rund um die Bewerbung: Lebenslauf, Bewerbungsschreiben...
http://www.lernkompass-jobs.de/berufe/
Dies ist eine Überblicksseite für unser "Berufe A-Z". Schüler finden hier Informationen zu Ausbildungsberufen: Ausbildungsdauer, Durchschnittsgehälter, Voraussetzungen...
Die Banner sollen folgende Maße haben. Breite 300, Höhe 250

```html
<!DOCTYPE html>
<html lang="de">
<head>
<meta charset="utf-8">
<title>Lernkompass Banner</title>
<link rel="stylesheet" href="https://fonts.googleapis.com/css2?family=Fira+Sans:ital,wght@1,800&family=Roboto+Condensed:wght@700&display=swap">
<style>
  :root {
    --canvas: #ffffff;
    --banner-bg: #075b70;
    --accent: #8dc71f;
    --text-light: #ffffff;
    --logo-bg: #a9b5bd;
    --photo-hair: #c98a4e;
    --photo-skin: #f0c2a2;
    --photo-shirt: #3e77b8;
    --photo-dark: #2a2a2a;
  }
  * { margin: 0; padding: 0; box-sizing: border-box; }
  html, body { width: 1200px; height: 1029px; overflow: hidden; background: var(--canvas); }
  .canvas { position: relative; width: 1200px; height: 1029px; }
  .banner {
    position: absolute; width: 514px; height: 428px;
    background: var(--banner-bg); overflow: hidden;
  }
  .banner--berufe { left: 60px; top: 58px; }
  .banner--stellen { left: 627px; top: 58px; }
  .banner--bewerben { left: 60px; top: 535px; }
  .banner--traumberuf { left: 627px; top: 535px; }

  .headline {
    position: absolute; z-index: 2;
    font-family: "Fira Sans", sans-serif; font-style: italic; font-weight: 800;
    font-size: 40px; line-height: 58px; color: var(--accent); letter-spacing: 0.3px;
  }
  .benefits {
    position: absolute; z-index: 2; list-style: none;
    font-family: "Roboto Condensed", sans-serif; font-weight: 700;
    font-size: 28px; line-height: 51px; color: var(--text-light);
  }
  .cta {
    position: absolute; z-index: 2; left: 24px; top: 376px;
    font-family: "Roboto Condensed", sans-serif; font-weight: 700;
    font-size: 21px; color: var(--accent);
  }
  .photo {
    position: absolute; z-index: 1;
    border: 7px solid var(--text-light);
    border-radius: 46% 46% 0 0 / 30% 30% 0 0;
    background: linear-gradient(180deg, var(--photo-hair) 0%, var(--photo-skin) 38%, var(--photo-hair) 62%, var(--photo-shirt) 100%);
  }
  .photo--thumbs { left: 300px; top: 20px; width: 230px; height: 420px; }
  .photo--wave {
    left: 220px; top: 70px; width: 310px; height: 370px;
    background: linear-gradient(180deg, #d9b25e 0%, var(--photo-skin) 40%, var(--photo-dark) 70%, var(--photo-dark) 100%);
  }
  .brand {
    position: absolute; z-index: 3; left: 267px; top: 336px; width: 233px; height: 81px;
    background: var(--logo-bg); display: flex; align-items: center; justify-content: center;
    font-family: "Roboto Condensed", sans-serif; font-weight: 700; font-size: 30px;
    color: var(--text-light); letter-spacing: 0.5px;
  }
</style>
</head>
<body>
<main class="canvas">

  <section class="banner banner--berufe">
    <h2 class="headline" style="left:17px; top:18px;">Ausbildungs-<br>beruf finden</h2>
    <ul class="benefits" style="left:17px; top:170px;">
      <li>- Berufe von A-Z</li>
      <li>- komplette Übersicht</li>
    </ul>
    <div class="photo photo--thumbs" role="img" aria-label="Foto: junge Frau mit langen rotblonden Haaren lächelt und zeigt Daumen hoch"></div>
    <p class="cta">&gt;&gt; jetzt loslegen</p>
    <div class="brand">Lernkompass</div>
  </section>

  <section class="banner banner--stellen">
    <h2 class="headline" style="left:104px; top:8px;">Stellenangebote</h2>
    <ul class="benefits" style="left:14px; top:229px;">
      <li>- Ausbildung</li>
      <li>- Duales System</li>
    </ul>
    <div class="photo photo--wave" role="img" aria-label="Foto: junge blonde Frau in schwarzer Jacke lächelt und breitet die Arme aus"></div>
    <p class="cta">&gt;&gt; jetzt loslegen</p>
    <div class="brand">Lernkompass</div>
  </section>

  <section class="banner banner--bewerben">
    <h2 class="headline" style="left:20px; top:22px;">Jetzt richtig<br>bewerben</h2>
    <ul class="benefits" style="left:38px; top:172px;">
      <li>- kostenlose Tipps</li>
      <li>- aktuelle Trends</li>
    </ul>
    <div class="photo photo--thumbs" role="img" aria-label="Foto: junge Frau mit langen rotblonden Haaren lächelt und zeigt Daumen hoch"></div>
    <p class="cta">&gt;&gt; jetzt loslegen</p>
    <div class="brand">Lernkompass</div>
  </section>

  <section class="banner banner--traumberuf">
    <h2 class="headline" style="left:20px; top:22px;">Finde deinen<br>Traumberuf</h2>
    <ul class="benefits" style="left:72px; top:172px;">
      <li>- ist kostenlos</li>
      <li>- Macht Spaß</li>
    </ul>
    <div class="photo photo--thumbs" role="img" aria-label="Foto: junge Frau mit langen rotblonden Haaren lächelt und zeigt Daumen hoch"></div>
    <p class="cta">&gt;&gt; jetzt loslegen</p>
    <div class="brand">Lernkompass</div>
  </section>

</main>
</body>
</html>
```